Weight Loss Challenge Social Media Graphics

Create 6-7 individual social media graphics (square size) to encourage folks to join our weight loss challenge. For the color scheme of the graphics, use the color palette attached

Note: each graphic can contain any of the stock photography attached or just the single picture of me (brown shirt) but a few should be ONLY the text
For some graphics we can say: JOIN US!
For some graphics, use only TEXT based

Target Market(s)

primarily women who want to get healthy

Industry/Entity Type

health and weight loss

Requirements
Must have
• The largest text should be: Ninety Days Bold

```html
<!DOCTYPE html>
<html lang="en">
<head>
<meta charset="UTF-8">
<title>Ninety Days Bold – Challenge Announcement</title>
<link href="https://fonts.googleapis.com/css2?family=Oswald:wght@600;700&family=Montserrat:wght@500&display=swap" rel="stylesheet">
<style>
  :root {
    --mauve-deep: #ad8b86;
    --mauve-soft: #c09c93;
    --blush-text: #fde1ea;
    --dot: #f6e3ea;
    --shadow: rgba(58, 28, 34, 0.6);
  }
  html, body {
    margin: 0;
    padding: 0;
    overflow: hidden;
    background: var(--mauve-deep);
  }
  .canvas {
    position: relative;
    width: 1200px;
    height: 1200px;
    overflow: hidden;
    background: var(--mauve-deep);
  }
  .backdrop {
    position: absolute;
    inset: 0;
    width: 1200px;
    height: 1200px;
  }
  .backdrop .wave { fill: var(--mauve-soft); }
  .backdrop .bubble { fill: var(--mauve-soft); }
  .backdrop .dot { fill: var(--dot); }
  .headline {
    position: absolute;
    left: 166px;
    top: 392px;
    margin: 0;
    font-family: "Oswald", "Arial Narrow", sans-serif;
    font-weight: 700;
    font-size: 190px;
    line-height: 211px;
    letter-spacing: 1px;
    text-transform: uppercase;
    color: var(--blush-text);
    text-shadow: 7px 8px 9px var(--shadow);
  }
  .headline span { display: block; white-space: nowrap; }
  .headline .headline-second { padding-left: 100px; }
  .start-date {
    position: absolute;
    right: 160px;
    top: 866px;
    margin: 0;
    font-family: "Montserrat", "Helvetica Neue", sans-serif;
    font-weight: 500;
    font-size: 31px;
    letter-spacing: 0.5px;
    color: var(--blush-text);
  }
</style>
</head>
<body>
  <main class="canvas">
    <svg class="backdrop" viewBox="0 0 1200 1200" aria-hidden="true">
      <path class="wave" d="M0,0 H262 C252,215 360,370 600,515 C830,655 850,840 760,915 C665,985 330,915 0,875 Z"/>
      <circle class="bubble" cx="519" cy="13" r="105"/>
      <circle class="bubble" cx="855" cy="405" r="117"/>
      <circle class="bubble" cx="1024" cy="909" r="47"/>
      <circle class="bubble" cx="333" cy="1180" r="135"/>
      <g class="dot-grid dot-grid--top">
        <circle class="dot" cx="1125" cy="56" r="4.5"/>
        <circle class="dot" cx="1145" cy="56" r="4.5"/>
        <circle class="dot" cx="1125" cy="76" r="4.5"/>
        <circle class="dot" cx="1145" cy="76" r="4.5"/>
        <circle class="dot" cx="1125" cy="96" r="4.5"/>
        <circle class="dot" cx="1145" cy="96" r="4.5"/>
        <circle class="dot" cx="1125" cy="116" r="4.5"/>
        <circle class="dot" cx="1145" cy="116" r="4.5"/>
        <circle class="dot" cx="1125" cy="140" r="4.5"/>
      </g>
      <g class="dot-grid dot-grid--bottom">
        <circle class="dot" cx="75" cy="1055" r="4.5"/>
        <circle class="dot" cx="75" cy="1075" r="4.5"/>
        <circle class="dot" cx="55" cy="1075" r="4.5"/>
        <circle class="dot" cx="75" cy="1095" r="4.5"/>
        <circle class="dot" cx="55" cy="1095" r="4.5"/>
        <circle class="dot" cx="75" cy="1115" r="4.5"/>
        <circle class="dot" cx="55" cy="1115" r="4.5"/>
        <circle class="dot" cx="75" cy="1135" r="4.5"/>
        <circle class="dot" cx="55" cy="1135" r="4.5"/>
      </g>
    </svg>

    <h1 class="headline">
      <span class="headline-first">Ninety</span>
      <span class="headline-second">Days Bold</span>
    </h1>
    <p class="start-date">Begins Monday, Jan 6th</p>
  </main>
</body>
</html>
```